Full-Size Brochure for Medical Mobile App (Zorvek)

I am looking for a full-size brochure for a mobile app (Zorvek - not on Maltoby) that is used in the pharmaceutical clinical trial industry of 8 pages (Letter format). The total content is about 1000 words (attached). This brochure needs to be an attractive design and the design should support the content. The goal of the brochure to persuade people to try the application, so it needs to be inviting to read and save the brochure. We need to print this as well as be able to distribute this as a PDF, so we need a small size PDF file and a high res print-ready PDF. The brochure needs to be designed in accordance with the brandbook (attached). A mockup (for screenshots) of the application can be found at: https://proto.quenvia-example.net/view/3c9a1e2d-58b4-4f0e-a7d1-9e2b6f4c8a10/

Target Market(s)

Pharmaceutical companies. CRO's and Central Laboratories

Industry/Entity Type

Medical And Science

Other font styles liked:
• See brandbook

Requirements
Must have
• Must have a sleek design that invites to read the content.
Nice to have
• Some added (generic) graphics to support the content.

```html
<!DOCTYPE html>
<html lang="en">
<head>
<meta charset="utf-8">
<title>Kelvaro Brochure</title>
<link href="https://fonts.googleapis.com/css2?family=Montserrat:wght@300;400;600;700;800&family=Oswald:wght@500;600&family=Roboto:wght@400;500;700&display=swap" rel="stylesheet">
<style>
:root{
  --bg:#ececec;
  --blue:#1d4fa8;
  --navy:#0f3a8c;
  --deep:#0b2d72;
  --cyan:#35bde6;
  --sky:#d9f1fb;
  --ink:#1c2333;
  --white:#ffffff;
}
*{box-sizing:border-box;margin:0;padding:0}
html,body{width:912px;height:1200px;overflow:hidden;background:var(--bg)}
body{position:relative;font-family:"Roboto",Arial,sans-serif;color:var(--ink)}
.spread{position:absolute;left:40px;width:832px;height:538px;display:flex;box-shadow:0 10px 30px rgba(0,0,0,.25)}
.spread--outer{top:40px}
.spread--inner{top:622px}
.page{position:relative;width:416px;height:538px;overflow:hidden;background:var(--white)}
.page__bg{position:absolute;inset:0;width:100%;height:100%}
.brand{position:absolute;display:flex;align-items:center;gap:7px;font-family:"Montserrat",sans-serif;font-weight:700;font-size:22px;color:var(--white)}
.brand__dot{width:16px;height:16px;border-radius:50%;background:var(--white)}
.brand--dark{color:var(--blue)}
.brand--dark .brand__dot{background:var(--cyan)}
.photo{position:absolute}
.url-bar{position:absolute;left:0;right:0;height:28px;background:var(--cyan);color:var(--white);font-family:"Montserrat",sans-serif;font-size:12px;font-weight:600;display:flex;align-items:center;justify-content:center;letter-spacing:.3px}
.base-strip{position:absolute;left:0;right:0;bottom:0;background:var(--sky)}
/* back cover */
.contact{position:absolute;left:0;right:0;top:376px;text-align:center}
.contact__label{font-family:"Montserrat",sans-serif;font-weight:800;font-size:16px;color:var(--cyan)}
.contact__note{font-size:9px;color:var(--ink);margin-top:3px}
.contact__phone{font-family:"Montserrat",sans-serif;font-weight:800;font-size:27px;color:var(--navy);margin-top:4px}
/* front cover */
.badge{position:absolute;width:58px;height:58px;border-radius:50%;background:#1b2230}
.tagline{position:absolute;left:0;right:0;top:370px;text-align:center;color:var(--navy)}
.tagline__lead{font-family:"Montserrat",sans-serif;font-weight:300;font-size:19px;color:var(--ink)}
.tagline__main{font-family:"Montserrat",sans-serif;font-weight:800;font-size:30px;letter-spacing:.5px}
/* inner left */
.intro{position:absolute;left:30px;right:30px;top:92px}
.intro__lead{font-weight:700;font-style:italic;font-size:10.5px;line-height:1.45;color:var(--navy);text-align:justify}
.intro__body{margin-top:12px;font-size:9.6px;line-height:1.5;text-align:justify}
/* inner right */
.problems__title{position:absolute;left:28px;top:82px;color:var(--white)}
.problems__kicker{font-family:"Montserrat",sans-serif;font-weight:400;font-size:15px}
.problems__head{font-family:"Oswald",sans-serif;font-weight:600;font-size:22px;line-height:1.2;text-transform:uppercase}
.bulb{position:absolute;left:36px;top:176px}
.problems__list{position:absolute;left:34px;right:22px;top:256px;list-style:none;font-size:7.4px;line-height:1.4}
.problems__list li{position:relative;padding-left:8px;margin-bottom:3px}
.problems__list li::before{content:"";position:absolute;left:0;top:4px;width:3px;height:3px;border-radius:50%;background:var(--ink)}
.problems__close{position:absolute;left:34px;right:22px;top:470px;font-size:7.6px;font-weight:700;color:var(--ink)}
</style>
</head>
<body>

<section class="spread spread--outer">
  <!-- back cover -->
  <article class="page page--back">
    <svg class="page__bg" viewBox="0 0 416 538" preserveAspectRatio="none" aria-hidden="true">
      <defs>
        <linearGradient id="backBlue" x1="0" y1="0" x2="1" y2="1">
          <stop offset="0" stop-color="#163f94"/><stop offset="1" stop-color="#2a63c4"/>
        </linearGradient>
      </defs>
      <polygon points="0,0 416,0 416,300 0,350" fill="url(#backBlue)"/>
      <polygon points="0,350 416,300 416,538 0,538" fill="#ffffff"/>
    </svg>
    <div class="photo" role="img" aria-label="Photo of a tablet on a leather stand showing the login screen, with blood sample tubes behind" style="left:40px;top:110px;width:300px;height:230px;border-radius:12px;background:linear-gradient(160deg,#2b3e63 0%,#4a6ea8 55%,#a97a4d 100%)"></div>
    <div class="brand" style="left:34px;top:34px"><span class="brand__dot"></span>Kelvaro</div>
    <div class="contact">
      <div class="contact__label">MORE INFORMATION</div>
      <div class="contact__note">To learn more about the Kelvaro application and how it can help you, visit</div>
      <div class="contact__phone">CALL +1 (555) 014 2290</div>
    </div>
    <div class="url-bar" style="top:470px">www.trialvantrent.example</div>
    <div class="base-strip" style="height:40px;top:498px"></div>
  </article>

  <!-- front cover -->
  <article class="page page--front">
    <svg class="page__bg" viewBox="0 0 416 538" preserveAspectRatio="none" aria-hidden="true">
      <polygon points="0,0 416,0 416,230 0,270" fill="#1a4aa3"/>
      <polygon points="0,270 416,230 416,538 0,538" fill="#ffffff"/>
    </svg>
    <div class="photo" role="img" aria-label="Faint blue-toned photo of a person walking up a staircase" style="left:0;top:0;width:416px;height:140px;background:linear-gradient(180deg,rgba(120,150,210,.35),rgba(26,74,163,0))"></div>
    <div class="brand" style="left:148px;top:60px;font-size:26px"><span class="brand__dot" style="width:20px;height:20px"></span>Kelvaro</div>
    <div class="photo" role="img" aria-label="White tablet showing the app login screen" style="left:68px;top:112px;width:280px;height:190px;border-radius:14px;background:linear-gradient(180deg,#e9edf3 0%,#ffffff 30%,#dfe4ea 100%);border:6px solid #f4f6f8;box-shadow:0 6px 16px rgba(0,0,0,.25)"></div>
    <div class="badge" style="left:42px;top:148px"></div>
    <div class="tagline">
      <div class="tagline__lead">Global Leader in rentals for</div>
      <div class="tagline__main">CLINICAL TRIALS</div>
    </div>
    <div class="url-bar" style="top:452px;background:linear-gradient(90deg,var(--blue),var(--cyan))">www.trialvantrent.example</div>
    <div class="base-strip" style="height:58px;top:480px"></div>
  </article>
</section>

<section class="spread spread--inner">
  <!-- inner left -->
  <article class="page page--intro">
    <svg class="page__bg" viewBox="0 0 416 538" preserveAspectRatio="none" aria-hidden="true">
      <polygon points="0,330 416,300 416,538 0,538" fill="#1d4fa8"/>
    </svg>
    <div class="brand brand--dark" style="left:128px;top:36px;font-size:26px"><span class="brand__dot" style="width:22px;height:22px"></span>Kelvaro</div>
    <div class="intro">
      <p class="intro__lead">In the world of clinical trials, the loss of specimens can be catastrophic. Not only the financial implications, but especially the scientific value of a unique specimen can make them priceless. And yet, many clinical trials still rely on specimen collection containers that are labeled at the site using blank labels and sharpies.</p>
      <p class="intro__body">Handwritten specimen labels have the highest failure rates when it comes to sample loss. But the problem doesn't stop with just the labels. When the samples are shipped to the laboratory for analysis, a handwritten requisition form generally accompanies them. So, even though Clinical Trial Management Software (CTMS) is implemented in order to manage, track and report on collected sample data, there is still a blind spot from the moment the sample is collected, until it is entered into the Laboratory Information Management System (LIMS).</p>
    </div>
    <div class="photo" role="img" aria-label="Tablets showing the app's study selection and subject screens" style="left:50px;top:300px;width:316px;height:170px;border-radius:12px;background:linear-gradient(180deg,#f2f4f7 0%,#dde3ea 100%);border:6px solid #e8ebef;box-shadow:0 6px 16px rgba(0,0,0,.3)"></div>
    <div class="url-bar" style="top:486px;background:transparent">www.trialvantrent.example</div>
    <div class="base-strip" style="height:26px;background:var(--cyan)"></div>
  </article>

  <!-- inner right -->
  <article class="page page--problems">
    <svg class="page__bg" viewBox="0 0 416 538" preserveAspectRatio="none" aria-hidden="true">
      <polygon points="0,0 416,0 416,70 0,250" fill="#1d4fa8"/>
      <polygon points="0,250 120,198 0,250" fill="#1d4fa8"/>
    </svg>
    <div class="photo" role="img" aria-label="Photo of a gloved hand holding a blood sample tube" style="left:250px;top:0;width:166px;height:190px;background:linear-gradient(150deg,#3a6cc0 0%,#d5dbe6 60%,#8c1f2a 100%);clip-path:polygon(100% 0,100% 60%,0 100%,30% 0)"></div>
    <div class="brand" style="left:28px;top:32px;font-size:26px"><span class="brand__dot" style="width:20px;height:20px"></span>Kelvaro</div>
    <div class="problems__title">
      <div class="problems__kicker">IDENTIFIED PROBLEMS</div>
      <div class="problems__head">In the industry<br>today</div>
    </div>
    <svg class="bulb" width="22" height="28" viewBox="0 0 22 28" aria-hidden="true">
      <circle cx="11" cy="10" r="8" fill="#ffffff" stroke="#35bde6" stroke-width="2"/>
      <rect x="7" y="18" width="8" height="6" rx="1" fill="#35bde6"/>
    </svg>
    <ul class="problems__list">
      <li>Over half of all identification errors in the lab result from bad specimen labels (i.e., illegible handwriting, spelling errors, inconsistent date notation, wrong subject ID, etc.)</li>
      <li>Few or no barcodes on specimen labels. Barcodes allow for subject/specimen information to be transmitted and stored electronically, reducing the need for human manual data entry, and centralizing the information in a secure database</li>
      <li>Insufficient number of barcodes complicates the process of correlating information to provide a clear chain-of-custody record, which in turn complicates attempts to identify and correct errors that may already exist but have gone undetected</li>
      <li>Clinical trial sites must allocate valuable site space to accommodate influx of study-specific collection kits and materials. This is not a smart or efficient use of lab space.</li>
      <li>Following or amending protocol is time-consuming, slow, and expensive (i.e., in the event of a change of protocol, current kits must be discarded, and new kits must be sourced, packed, and shipped to the site, old protocol binders must be discarded, and new protocol binders must be printed and shipped to the site, etc.)</li>
      <li>Project managers cannot get real-time, up-to-date insight into the progress of all sites participating in the study. The transfer of information is delayed.</li>
      <li>Laboratories miss the opportunity to conserve valuable time because they are not provided with accurate forecasts regarding when certain samples will be arriving at their facility</li>
    </ul>
    <p class="problems__close">Kelvaro was designed to fill the information gap between the time of sample collection and arrival at the lab.</p>
    <div class="url-bar" style="top:490px">www.trialvantrent.example</div>
    <div class="base-strip" style="height:20px;background:var(--sky)"></div>
  </article>
</section>

</body>
</html>
```